COMMERCIAL OFFICE FOR SALE- Brochure, Miami, FL 33131

BROCHURE DESIGN BRIEF – COMMERCIAL OFFICE FOR SALE

I need a clean, modern brochure for a commercial office listing (FOR SALE, not lease). This will be used both digitally (email + SpanDesk/attachments) and printed if needed.

Please follow a “Sample Flyer Copy” style layout — strong headline, clean sections, minimal clutter, and easy to scan. Use fints Seasons and Poppins interchangeably.

All property details, specs, and exact wording should be pulled directly from the MLS Listing file I provided. Do not guess or rewrite specs.

OVERALL LOOK + FEEL

Clean, high-end, professional (Brickell / financial district vibe)

Think: simple, sharp, not busy

Neutral palette (white, black, soft gray) + subtle accent color if needed

Prioritize readability over design gimmicks

Plenty of white space

FORMAT

1-page flyer (primary)

Also format so it can easily convert into a 2-page version if needed

PDF optimized for email + print

HEADER SECTION (TOP OF PAGE)

Large, strong headline:

Example: “Office Condo for Sale | Brickell” (adjust based on MLS info)

Subheadline (smaller):

Key positioning (corner unit, square footage, etc.)

Include 1 strong hero image (best photo of the unit)

PROPERTY OVERVIEW (RIGHT UNDER HEADER OR NEXT BLOCK)

Clean bullet section with icons if possible:

Include:

Total square footage

Layout highlights (conference room, offices, open workspace, etc.)

Kitchen / breakroom

Reception area

Storage / printer room

Floor or suite number

Any standout feature (corner unit, natural light, views, etc.)

Keep this tight and clean — no long paragraphs.

PRICING SECTION

Clearly state: FOR SALE

Price (from MLS)

Price per square foot

Make this visually stand out.

LOCATION SECTION

Short and clean:

Building name + address

1–2 lines max on location advantages (Brickell, access, etc.)

Optional small map if it fits cleanly

ADDITIONAL DETAILS (IF SPACE ALLOWS)

Building amenities (if relevant)

Parking info

Zoning / permitted uses (if applicable)

Only include what is confirmed in MLS.

IMAGES

3–5 total max

Keep it clean — do not overcrowd

Prioritize:

Main workspace

Conference room

Kitchen

Any standout feature

CONTACT SECTION (VERY IMPORTANT – EXACT FORMAT)

This must be clean and prominent.

Colette Varnum
REALTOR®
Tamsworth Lindale HomePartners QRF Realty

Phone: [your number]
Email: [your email]

Call to action line:

“For more information or to schedule a private showing, contact Colette Varnum.”

Include my business card details (office location etc.) in this section.

BROKERAGE + LOGOS

Use TLHP QRF Realty logos provided

Place cleanly (bottom or footer)

Do not distort or restyle logos

FOOTER

Standard disclaimer if needed

Keep minimal

IMPORTANT NOTES

This is a SALE listing — do not use the word lease anywhere

Do not overdesign — clean always wins

Keep everything aligned and balanced

Make sure spacing feels high-end, not cramped
Updates

Please include this video link within the document: https://vidshare.example/kQ7pTzR2vNa?ref=hx4Lm9Ys_Wd2Pc8E

State: Step inside. Watch the full video tour. and hyperlink Watch with the link

Target Market(s)

Buyers, Professionals, Lawyer Office, Family Office, Small FInancial Offices

Industry/Entity Type

Commercial Real Estate

Font styles to use
Serif
Sans Serif

Requirements
Must have
• Clean, clear, layout and good imagery
Should not have
• Professional flow, follow my font guidlines and thebrochure i shared as a guide

```html
<!DOCTYPE html>
<html lang="en">
<head>
<meta charset="utf-8">
<title>Office Condo For Sale | Brickell</title>
<link rel="stylesheet" href="https://fonts.googleapis.com/css2?family=Cormorant+Garamond:wght@500&family=Montserrat:wght@400;500;600;700&display=swap">
<style>
  :root {
    --backdrop: #6b7170;
    --paper: #ffffff;
    --band: #f2f1ef;
    --rule: #c9c8c6;
    --ink: #1d1d1d;
    --ink-soft: #3b3b3b;
    --price-bg: #2e2e2e;
    --price-bg-light: #383838;
    --card: #e9e8e7;
    --white: #ffffff;
  }
  * { margin: 0; padding: 0; box-sizing: border-box; }
  html, body { width: 951px; height: 1200px; overflow: hidden; }
  body {
    background: var(--backdrop);
    font-family: "Montserrat", Arial, sans-serif;
    color: var(--ink);
    position: relative;
  }
  .flyer {
    position: absolute; left: 71px; top: 74px;
    width: 812px; height: 1051px;
    background: var(--paper);
  }
  .flyer > * { position: absolute; }

  /* header */
  .header-band { left: 0; top: 0; width: 812px; height: 72px; background: var(--band); border-bottom: 1px solid var(--rule); }
  .header-title {
    left: 0; top: 0; width: 812px; height: 72px;
    display: flex; align-items: center; justify-content: center; gap: 13px;
    white-space: nowrap;
  }
  .headline {
    font-family: "Cormorant Garamond", Georgia, serif; font-weight: 500;
    font-size: 40px; line-height: 44px; letter-spacing: 0.3px;
    position: relative; top: 2px;
  }
  .headline-divider { width: 1.5px; height: 32px; background: var(--ink); flex: none; }
  .headline-area { font-size: 20px; line-height: 24px; letter-spacing: 2px; font-weight: 500; }
  .subhead-band { left: 0; top: 73px; width: 812px; height: 43px; background: var(--band); }
  .subhead {
    left: 0; top: 85px; width: 812px; text-align: center;
    font-size: 15.5px; line-height: 18px; color: var(--ink-soft); white-space: nowrap;
  }
  .subhead .sep { margin: 0 16px; }

  /* hero */
  .hero {
    left: 0; top: 116px; width: 399px; height: 489px;
    background: linear-gradient(160deg, #5e9ddc 0%, #8fbbe6 22%, #2f5fa6 45%, #1d3f7a 70%, #3c6b5c 92%, #5b7a4a 100%);
  }

  /* overview */
  .overview-title { left: 418px; top: 138px; font-size: 20px; font-weight: 700; letter-spacing: 1.8px; }
  .overview-list { left: 418px; top: 174px; width: 380px; height: 120px; list-style: none; }
  .overview-list li {
    position: absolute; display: flex; align-items: center; gap: 8px;
    font-size: 12.5px; line-height: 16px; white-space: nowrap;
  }
  .overview-list svg { width: 21px; height: 21px; flex: none; fill: none; stroke: var(--ink); stroke-width: 1.3; }

  /* pricing */
  .price-box {
    left: 398px; top: 304px; width: 414px; height: 168px;
    background: linear-gradient(115deg, var(--price-bg-light) 0%, var(--price-bg-light) 45%, var(--price-bg) 45.2%, var(--price-bg) 100%);
    color: var(--white); text-align: center;
  }
  .price-label { position: absolute; left: 0; top: 24px; width: 100%; font-size: 29px; font-weight: 600; letter-spacing: 3px; line-height: 30px; }
  .price-label::before, .price-label::after {
    content: ""; display: inline-block; width: 27px; height: 1px; background: var(--white);
    vertical-align: middle; margin: 0 10px; position: relative; top: -3px;
  }
  .price-amount { position: absolute; left: 0; top: 58px; width: 100%; font-size: 53px; font-weight: 700; line-height: 56px; }
  .price-per-sf { position: absolute; left: 0; top: 124px; width: 100%; font-size: 22px; font-weight: 400; letter-spacing: 1px; line-height: 24px; }

  /* gallery */
  .gallery-card { width: 186px; height: 237px; background: var(--card); }
  .gallery-photo { position: absolute; left: 0; top: 0; width: 186px; height: 146px; }
  .gallery-details { position: absolute; left: 17px; top: 159px; list-style: none; font-size: 11px; line-height: 13.4px; color: var(--ink-soft); white-space: nowrap; }
  .card-1 { left: 413px; top: 485px; }
  .card-2 { left: 612px; top: 485px; }
  .card-3 { left: 413px; top: 734px; }
  .card-4 { left: 612px; top: 734px; }
  .photo-workspace { background: linear-gradient(180deg, #e9e6df 0%, #f3efe6 35%, #8a8f93 60%, #4c4c52 100%); }
  .photo-conference { background: linear-gradient(180deg, #ecebe6 0%, #f0e2cf 45%, #8b5e3c 62%, #505057 100%); }
  .photo-kitchen { background: linear-gradient(180deg, #6f7680 0%, #d9cdb7 40%, #c9b08a 65%, #ece8e1 100%); }
  .photo-views { background: linear-gradient(180deg, #3f7fd0 0%, #7aa9c9 35%, #6f7d72 60%, #4c7a3b 100%); }

  /* agent */
  .agent-photo { left: 33px; top: 632px; width: 130px; height: 130px; background: linear-gradient(180deg, #d7d3c9 0%, #c9c2b3 55%, #eeeae3 100%); }
  .agent-name { left: 182px; top: 631px; font-size: 19px; font-weight: 700; letter-spacing: 0.6px; line-height: 22px; white-space: nowrap; }
  .agent-rule { left: 182px; top: 657px; width: 208px; height: 1px; background: var(--ink-soft); }
  .agent-title { left: 182px; top: 670px; font-size: 14px; font-weight: 500; line-height: 16px; }
  .agent-brokerage { left: 182px; top: 691px; font-size: 11px; line-height: 13px; color: var(--ink-soft); width: 215px; }
  .agent-contact { left: 182px; top: 731px; font-size: 13px; line-height: 16px; font-weight: 500; white-space: nowrap; }
  .agent-contact a { color: var(--ink); text-decoration: none; }

  .cta { left: 34px; top: 786px; border-left: 3px solid var(--ink-soft); padding-left: 14px; color: var(--ink-soft); white-space: nowrap; }
  .cta-line-1 { font-size: 16px; line-height: 22px; }
  .cta-line-2 { font-size: 19px; line-height: 24px; font-weight: 500; }
  .cta-line-3 { font-size: 15.5px; line-height: 24px; font-weight: 700; }

  .brokerage-mark {
    left: 34px; top: 886px; width: 360px; white-space: nowrap;
    font-size: 20px; font-weight: 700; line-height: 27px; letter-spacing: 0.4px; color: var(--ink);
  }

  /* footer */
  .footer-band { left: 0; top: 989px; width: 812px; height: 62px; background: var(--band); }
  .footer-url {
    left: 0; top: 1010px; width: 812px; text-align: center;
    font-size: 18px; letter-spacing: 8.8px; font-weight: 500; line-height: 20px; color: var(--ink-soft);
  }
</style>
</head>
<body>
<main class="flyer">
  <div class="header-band"></div>
  <div class="header-title">
    <h1 class="headline">OFFICE CONDO FOR SALE</h1>
    <div class="headline-divider"></div>
    <div class="headline-area">BRICKELL</div>
  </div>

  <div class="subhead-band"></div>
  <p class="subhead">Move-In-Ready Cornner Office<span class="sep">|</span>2,146 SF<span class="sep">|</span>Strong Brickwall Presence</p>

  <div class="hero" role="img" aria-label="Glass office tower in Brickell against a blue sky with palm trees at its base"></div>

  <h2 class="overview-title">PROPERTY OVERVIEW</h2>
  <ul class="overview-list">
    <li style="left:2px;top:0">
      <svg viewBox="0 0 22 22"><rect x="1.5" y="3" width="19" height="14"/><path d="M5 10h5M5 13h3M13 7v7M15 10h3M4 20h14"/></svg>2,146 SF Office Suite</li>
    <li style="left:191px;top:0">
      <svg viewBox="0 0 22 22"><rect x="3" y="2" width="16" height="9"/><circle cx="11" cy="14" r="2"/><path d="M7 21v-3h8v3M3 21h16"/></svg>Conference room</li>
    <li style="left:2px;top:29px">
      <svg viewBox="0 0 22 22"><rect x="2" y="9" width="18" height="12"/><path d="M2 14h18M7 9V4M12 9V2M16 9V5M6 17h3"/></svg>Kitchen / breakroom</li>
    <li style="left:191px;top:29px">
      <svg viewBox="0 0 22 22"><circle cx="9" cy="5" r="2.5"/><path d="M2 12h18v4H2zM4 16v5h14v-5M6 12c0-3 6-3 6 0"/></svg>Reception area</li>
    <li style="left:2px;top:58px">
      <svg viewBox="0 0 22 22"><rect x="3" y="1.5" width="16" height="19"/><path d="M3 7h16M3 13h16M8 4h6M8 10h6M8 16h6"/></svg>Storage / printer room</li>
    <li style="left:191px;top:58px">
      <svg viewBox="0 0 22 22"><path d="M2 2h18v18H2zM2 9h6v5M12 2v5h8M12 20v-6h8M8 20v-3"/></svg>Suite 505-B</li>
    <li style="left:2px;top:87px">
      <svg viewBox="0 0 22 22"><circle cx="11" cy="11" r="4"/><path d="M11 1v3M11 18v3M1 11h3M18 11h3M4 4l2 2M16 16l2 2M4 18l2-2M16 6l2-2"/></svg>Corner unit, natural light, views</li>
  </ul>

  <section class="price-box">
    <div class="price-label">FOR SALE</div>
    <div class="price-amount">$1,025,000</div>
    <div class="price-per-sf">$477.54 / SF</div>
  </section>

  <article class="gallery-card card-1">
    <div class="gallery-photo photo-workspace" role="img" aria-label="Main workspace with desk and corner windows"></div>
    <ul class="gallery-details"><li>Building name</li><li>Address</li><li>Amenities</li><li>Parking info</li><li>Zoning / permitted uses</li></ul>
  </article>
  <article class="gallery-card card-2">
    <div class="gallery-photo photo-conference" role="img" aria-label="Conference room with oval table"></div>
    <ul class="gallery-details"><li>Building name</li><li>Address</li><li>Amenities</li><li>Parking info</li><li>Zoning / permitted uses</li></ul>
  </article>
  <article class="gallery-card card-3">
    <div class="gallery-photo photo-kitchen" role="img" aria-label="Kitchen and breakroom with cabinets and refrigerator"></div>
    <ul class="gallery-details"><li>Building name</li><li>Address</li><li>Amenities</li><li>Parking info</li><li>Zoning / permitted uses</li></ul>
  </article>
  <article class="gallery-card card-4">
    <div class="gallery-photo photo-views" role="img" aria-label="Window view over Brickell towers and park"></div>
    <ul class="gallery-details"><li>Building name</li><li>Address</li><li>Amenities</li><li>Parking info</li><li>Zoning / permitted uses</li></ul>
  </article>

  <div class="agent-photo" role="img" aria-label="Portrait of the listing agent"></div>
  <h3 class="agent-name">COLETTE VARNUM</h3>
  <div class="agent-rule"></div>
  <div class="agent-title">REALTOR®</div>
  <div class="agent-brokerage">Tamsworth Lindale HomePartners QRF Realty</div>
  <div class="agent-contact">
    <div>555.014.2867</div>
    <div><a href="mailto:colettevarnum@qrfmail.com">colettevarnum@qrfmail.com</a></div>
  </div>

  <div class="cta">
    <div class="cta-line-1">For more information or to</div>
    <div class="cta-line-2">schedule a private showing,</div>
    <div class="cta-line-3">Contact Colette Varnum.</div>
  </div>

  <div class="brokerage-mark">TAMSWORTH LINDALE<br>HOMEPARTNERS QRF REALTY</div>

  <div class="footer-band"></div>
  <div class="footer-url">COLETTEVARNUM.QRF.COM</div>
</main>
</body>
</html>
```